GUARANTEED WordPress design needed for a sassy, confident charisma coach!

We need a website design for Marla Penrick's brand new, responsive, Wordpress website.
Marla is a trainer / coach who teaches people how to be more charismatic and runs events, publishes video courses and has an ongoing video blog. Her old website is here: www.marlapenrick.co.uk ... but it's now time to have a much better site!
We have a strong idea about the technical components of the website, but we need a designer's eye to create a great style for the site (and provide layered PSD files which our developers will then convert to HTML and CSS).
Marla's brand is sassy, brave, warm and confident. The videos on her existing site give quite a good feel for her personality. We need a clean, stylish and compelling page that isn't too corporate and captures her personality. Every element needs to feel coherent, from fonts and headings to colours and spacing.
The following sites are not exactly what Marla wants (and certainly aren't right in terms of colours) but they give you an idea of the kind of people she is competing against and the area she is operating in:
http://www.tessa-broughley.example/
http://rowanfelsby.example/
Ideally, you will have done something similar and be able to key in on exactly the kind of thing we want: we're not looking to reinvent the wheel. Hopefully you won't mind tweaking a few things if you are close to what we need.
More detail is provided in the word document attached. But in a nutshell we need: a banner, footer, sign-up strap, menu bar, signature and 4 different basic page types. We want bursts of bright colours, contrasted with black and white if possible - sorry we can't be more specific than that...
The word doc also contains some amateur mock-ups as well (the images are also just mockups at this stage) - but although these give a general sense of the structure what we are looking for, we are clearly not designers...so please help! We need a designer's touch!
Kind regards,
Corin
PS The layered PSD versions of the mockup files are available on Cloudvantre: https://files.cloudvantre.example/sh/k72pqa4w1zbtmrd/QXvenlr8Ty3PwMiU6Hs2kYfDb?dl=0
Target Market(s)
Entrepreneurs who need to sell themselves.
Number of Pages Required
4 page

```html
<!DOCTYPE html>
<html lang="en">
<head>
<meta charset="utf-8">
<title>Marla Penrick – Attract, Connect, Influence</title>
<link href="https://fonts.googleapis.com/css2?family=Great+Vibes&family=Kalam:wght@700&family=Open+Sans:wght@300;400;600;700&display=swap" rel="stylesheet">
<style>
:root{
  --ink:#2b2b2b;
  --muted:#777;
  --line:#e2e2e2;
  --red:#e8443a;
  --cyan:#2fc3e6;
  --orange:#f2a516;
  --dark:#3a3a3a;
  --footer:#2e2e2e;
  --band:#d9d9d9;
  --paper:#ffffff;
  --pale:#f4f4f4;
}
*{box-sizing:border-box;margin:0;padding:0}
html,body{width:1200px;height:3428px;overflow:hidden;background:var(--paper)}
body{font-family:"Open Sans",Arial,sans-serif;color:var(--ink);position:relative}

/* header */
.site-header{position:absolute;top:0;left:0;width:1200px;height:62px;border-bottom:2px solid var(--line);display:flex;align-items:center;justify-content:space-between;padding:0 72px}
.brand{display:flex;align-items:center;gap:10px;font-family:"Open Sans",Arial,sans-serif;font-weight:600;font-size:24px;color:var(--red)}
.brand-dot{width:12px;height:12px;border-radius:50%;background:var(--red)}
.main-nav{display:flex;gap:34px;font-weight:700;font-size:15px;letter-spacing:.5px}
.main-nav a{color:var(--ink);text-decoration:none}

/* hero */
.hero{position:absolute;top:64px;left:0;width:1200px;height:536px}
.hero-title{position:absolute;left:72px;top:120px;font-family:"Great Vibes",cursive;font-weight:400;color:var(--ink);line-height:.9}
.hero-title span{display:block}
.hero-title .w1{font-size:96px}
.hero-title .w2{font-size:110px;margin-left:50px}
.hero-title .w3{font-size:120px;margin-left:90px}
.hero-portrait{position:absolute;left:800px;top:20px;width:290px;height:516px;background:linear-gradient(180deg,#6d5246 0%,#d9b29a 30%,#e33b3b 55%,#c92c2c 100%);border-radius:150px 150px 0 0}

/* sign-up strap */
.strap{position:absolute;top:600px;left:0;width:1200px;height:280px;background:var(--cyan);color:#fff}
.strap-visual{position:absolute;left:110px;top:24px;width:320px;height:230px}
.strap-copy{position:absolute;left:480px;top:38px;width:620px;font-size:21px;line-height:1.35;font-weight:400}
.optin{position:absolute;left:480px;top:140px;display:flex;align-items:center;gap:12px}
.field{width:200px;height:44px;background:#fff;border:1px solid #d5d5d5;color:var(--muted);font-size:14px;padding:12px 14px}
.yes-btn{width:96px;height:96px;border-radius:50%;background:var(--red);border:4px solid #fff;color:#fff;font-weight:700;font-size:15px;display:flex;align-items:center;justify-content:center;text-align:center;line-height:1.1;margin-left:16px}
.strap-note{position:absolute;left:480px;top:226px;font-size:13px;color:#e9f9fd}

/* posts */
.posts{position:absolute;top:935px;left:72px;width:716px}
.post{height:685px;border-bottom:2px solid var(--line);margin-bottom:20px}
.post:nth-child(2){height:720px}
.post-title{font-family:"Kalam",cursive;font-weight:700;font-size:30px;color:var(--ink);margin-top:14px;line-height:1.2}
.byline{font-size:12px;color:var(--muted);margin:4px 0 14px}
.post-banner{width:716px;height:322px;color:#fff;padding:28px 36px;font-weight:400;font-size:50px;line-height:1.15;position:relative}
.banner-red{background:linear-gradient(90deg,#e9473d 0%,#e9473d 60%,#d9534a 100%)}
.banner-cyan{background:linear-gradient(90deg,#2fc3e6 0%,#2fc3e6 60%,#8fd8ea 100%)}
.banner-orange{background:linear-gradient(90deg,#f2a516 0%,#f2a516 62%,#c9862a 100%)}
.post-banner .figure{position:absolute;right:0;top:0;width:260px;height:322px;background:linear-gradient(180deg,rgba(0,0,0,.05),rgba(0,0,0,.22))}
.excerpt{font-size:13px;line-height:1.6;color:#555;margin:18px 0 22px}
.read-more{display:inline-flex;align-items:center;gap:10px;font-size:12px;color:var(--red);border:1px solid var(--red);padding:5px 10px;border-radius:3px}
.read-more i{width:0;height:0;border-left:7px solid var(--red);border-top:5px solid transparent;border-bottom:5px solid transparent}

.pagination{position:absolute;top:2958px;left:300px;display:flex;gap:8px;font-size:13px}
.pagination span{width:28px;height:28px;border-radius:50%;border:1px solid var(--line);display:flex;align-items:center;justify-content:center;color:var(--muted)}
.pagination .current{background:var(--red);border-color:var(--red);color:#fff}

/* sidebar */
.sidebar{position:absolute;top:940px;left:820px;width:308px}
.widget-head{background:var(--dark);color:#fff;font-family:"Kalam",cursive;font-weight:700;font-size:24px;text-align:center;padding:6px 0 2px;letter-spacing:1px}
.widget-head.red{color:var(--red);background:var(--pale)}
.widget-head.yellow{color:var(--red);background:#fff;border-top:3px solid var(--dark);border-bottom:3px solid var(--dark)}
.popular-label{color:var(--red);font-weight:700;font-size:15px;text-align:center;margin:10px 0 6px}
.popular li{list-style:none;font-size:13px;line-height:1.4;padding:9px 0;border-bottom:1px solid var(--line)}
.popular small{display:block;color:var(--red);font-weight:700;font-size:10px;margin-top:2px}
.tags{margin-top:30px}
.tag-cloud{text-align:center;padding:12px 6px;line-height:1.25;font-weight:700}
.tag-cloud span{display:inline-block;margin:0 4px}
.t-s{font-size:12px}.t-m{font-size:16px}.t-l{font-size:26px}
.event{margin-top:30px}
.event-card{margin-top:14px;width:308px;height:690px;background:linear-gradient(180deg,#3c3c3c 0%,#5a4a44 45%,#2a2a2a 100%);color:#fff;padding:28px 22px;position:relative}
.event-card h3{font-weight:700;font-size:32px;line-height:1.1}
.event-live{position:absolute;left:22px;top:400px;font-size:66px;font-weight:700;letter-spacing:2px}
.event-places{position:absolute;left:40px;top:490px;font-family:"Kalam",cursive;font-size:30px;line-height:1.1}
.event-btn{position:absolute;left:100px;top:590px;background:var(--cyan);padding:10px 18px;font-weight:700;font-size:20px;line-height:1.1;text-align:center}
.stories{margin-top:40px}
.quote{font-size:12px;font-style:italic;color:#555;line-height:1.6;padding:14px 4px;text-align:center}
.author{display:flex;align-items:center;gap:12px;justify-content:center}
.avatar{width:48px;height:48px;border-radius:50%;background:linear-gradient(180deg,#8a6a5a,#d3a98f)}
.author b{display:block;font-size:13px}.author small{font-size:11px;color:var(--muted)}
.story-link{display:block;margin:16px auto 0;width:230px;text-align:center;font-size:11px;color:var(--red);border:1px solid var(--red);border-radius:3px;padding:4px}
.dots{display:flex;gap:6px;justify-content:center;margin-top:14px}
.dots span{width:8px;height:8px;border-radius:50%;background:#ccc}.dots .on{background:var(--red)}

/* newsletter */
.newsletter{position:absolute;top:3040px;left:0;width:1200px;height:300px;background:var(--band);text-align:center}
.newsletter h2{font-family:"Kalam",cursive;font-weight:700;font-size:32px;line-height:1.2;color:var(--ink);width:900px;margin:36px auto 0}
.newsletter .optin{position:static;justify-content:center;margin-top:20px}
.newsletter .field{width:260px}
.newsletter-note{font-size:13px;color:#555;margin-top:6px}

/* footer */
.site-footer{position:absolute;top:3340px;left:0;width:1200px;height:88px;background:var(--footer);color:#ccc;font-size:13px;display:flex;align-items:center;justify-content:space-between;padding:0 72px}
.legal{display:flex;gap:34px}
.social{display:flex;gap:10px}
.social span{width:26px;height:26px;border-radius:3px;background:var(--red)}
</style>
</head>
<body>

<header class="site-header">
  <div class="brand"><span>Marla Penrick</span><span class="brand-dot"></span></div>
  <nav class="main-nav"><a href="#">EVENTS</a><a href="#">WORK WITH ME</a><a href="#">CORPORATE</a><a href="#">ABOUT</a><a href="#">CONTACT</a></nav>
</header>

<section class="hero">
  <h1 class="hero-title"><span class="w1">Attract</span><span class="w2">Connect</span><span class="w3">Influence</span></h1>
  <div class="hero-portrait" role="img" aria-label="Photo of Marla in a red dress, hand on hip, smiling"></div>
</section>

<section class="strap">
  <svg class="strap-visual" viewBox="0 0 320 230" role="img" aria-label="Desktop monitor showing a training video">
    <rect x="10" y="10" width="300" height="180" rx="8" fill="#222"/>
    <rect x="22" y="22" width="276" height="156" fill="#d9d9d9"/>
    <rect x="130" y="190" width="60" height="22" fill="#bbb"/>
    <rect x="100" y="212" width="120" height="8" rx="3" fill="#ccc"/>
  </svg>
  <p class="strap-copy">Learn how to unlock the superpower* of your charisma and win all the business you want with this FREE training.</p>
  <div class="optin"><div class="field">First name</div><div class="field">Email address</div><div class="yes-btn">YES<br>PLEASE!</div></div>
  <p class="strap-note">* Promise to only use your powers for good.</p>
</section>

<main class="posts">
  <article class="post">
    <h2 class="post-title">Public speaking...made easy</h2>
    <p class="byline">Written by Marla Penrick</p>
    <div class="post-banner banner-red" role="img" aria-label="Marla speaking with a microphone">PUBLIC SPEAKING...<br><br>MADE<br>EASY :-)<span class="figure"></span></div>
    <p class="excerpt">Lorem ipsum dolor sit amet, consectetur adipiscing elit. Praesent fringilla tortor et mi convallis, ut scelerisque dui rhoncus. Donec quis lorem malesuada, molestie metus id, vehicula lacus. Pellentesque ultricies venenatis ullamcorper. Sed metus ligula, pharetra id risus eu, fermentum auctor eros.</p>
    <span class="read-more">READ MORE <i></i></span>
  </article>
  <article class="post">
    <h2 class="post-title">Take charge of your style...Boost your confidence</h2>
    <p class="byline">Written by Marla Penrick</p>
    <div class="post-banner banner-cyan" role="img" aria-label="Marla in glasses beside a wardrobe sketch">TAKE CHARGE OF YOUR STYLE...<br>...BOOST YOUR<br>CONFIDENCE<span class="figure"></span></div>
    <p class="excerpt">Lorem ipsum dolor sit amet, consectetur adipiscing elit. Praesent fringilla tortor et mi convallis, ut scelerisque dui rhoncus. Donec quis lorem malesuada, molestie metus id, vehicula lacus. Pellentesque ultricies venenatis ullamcorper. Sed metus ligula, pharetra id risus eu, fermentum auctor eros.</p>
    <span class="read-more">READ MORE <i></i></span>
  </article>
  <article class="post">
    <h2 class="post-title">Unfulfilled? It's time to think about your values...</h2>
    <p class="byline">Written by Marla Penrick</p>
    <div class="post-banner banner-orange" role="img" aria-label="Marla thinking, holding a notepad">UNFULFILLED? IT'S TIME TO THINK ABOUT YOUR VALUES...<br>DO THIS EXERCISE NOW<span class="figure"></span></div>
    <p class="excerpt">Lorem ipsum dolor sit amet, consectetur adipiscing elit. Praesent fringilla tortor et mi convallis, ut scelerisque dui rhoncus. Donec quis lorem malesuada, molestie metus id, vehicula lacus. Pellentesque ultricies venenatis ullamcorper. Sed metus ligula, pharetra id risus eu, fermentum auctor eros.</p>
    <span class="read-more">READ MORE <i></i></span>
  </article>
</main>

<nav class="pagination"><span class="current">1</span><span>2</span><span>3</span><span>…</span><span>15</span><span>›</span></nav>

<aside class="sidebar">
  <section>
    <h3 class="widget-head">MARLA SAYS...</h3>
    <p class="popular-label">POPULAR</p>
    <ul class="popular">
      <li>Be more dog: 5 lessons we could learn from our best friends<small>TWEETS</small></li>
      <li>Are you letting your core beliefs hold you back?<small>SHARES</small></li>
      <li>How I learned to stop worrying and start NETWORKING!<small>VIEWS</small></li>
      <li>Blinky-eyelash face and other strange - but true - problems<small>COMMENTS</small></li>
    </ul>
  </section>
  <section class="tags">
    <h3 class="widget-head">TAGS</h3>
    <div class="tag-cloud">
      <span class="t-s">body language</span><br>
      <span class="t-l">capsule wardrobe</span><br>
      <span class="t-s">confidence</span><span class="t-s">handshake</span><span class="t-s">mindset</span><span class="t-s">vip</span><br>
      <span class="t-s">passion</span><span class="t-l">power pose</span><br>
      <span class="t-s">presentations</span><span class="t-s">presence</span><br>
      <span class="t-l">rapport</span><span class="t-s">spring wear</span><span class="t-s">style</span><br>
      <span class="t-m">value</span><span class="t-s">vision board</span><span class="t-s">warmth</span>
    </div>
  </section>
  <section class="event">
    <h3 class="widget-head yellow">COMING UP</h3>
    <div class="event-card" role="img" aria-label="Audience at a live charisma workshop">
      <h3>UNLOCK<br>THE<br>SUPERPOWER<br>OF<br>CHARISMA</h3>
      <span class="event-live">LIVE</span>
      <span class="event-places">Only 6<br>places left.</span>
      <span class="event-btn">LEARN<br>MORE</span>
    </div>
  </section>
  <section class="stories">
    <h3 class="widget-head red">SUCCESS STORIES</h3>
    <p class="quote">"I've never been a fashionista and my wardrobe was dominated by black... my appearance had become dull and uninteresting. One day with Marla and I was transformed!"</p>
    <div class="author"><div class="avatar" role="img" aria-label="Client portrait"></div><div><b>Odile</b><small>HR Director</small></div></div>
    <span class="story-link">Or read the full story, click here</span>
    <div class="dots"><span class="on"></span><span></span><span></span><span></span></div>
  </section>
</aside>

<section class="newsletter">
  <h2>Hey! Don't go without signing up because you'll miss out on exclusive offers, awesome tips, and weekly motivation in my fab newsletter *.</h2>
  <div class="optin"><div class="field">First name</div><div class="field">Email address</div><div class="yes-btn">YES<br>PLEASE!</div></div>
  <p class="newsletter-note">* And that'll make me sad :-(</p>
</section>

<footer class="site-footer">
  <div class="legal"><span>© 2016 Marla Penrick Ltd</span><span>PRIVACY POLICY</span><span>TERMS POLICY</span><span>DISCLAIMERS</span></div>
  <div class="social" aria-label="Social links"><span></span><span></span><span></span><span></span><span></span><span></span></div>
</footer>

</body>
</html>
```